Interior Design business card design

I am an interior decorator - dont want to specify decorating more just design.
Want organic looking logo - charcoal and white - with touch of lime green.
Like the idea of some sort of spiral in corner but writing in a line
want lower case, carlamintowe as one and designs in different font underneath. Maybe using c and m as logo.
More modern than traditional. My clients are mid to top end residential

Target Market(s)

medium to top end homeowners

Industry/Entity Type

Residential

Contact Information for Business Card

Carla Mintowe Designs
58 Fallowmere ave
Tindarra 2188 NSW
Tel 0417869214
carlamintowe@quellnet.com.au

Logo Text

Carla Mintowe Designs

Logo styles of interest
Abstract Logo
Lettermark Logo
Requirements
Must have
• Name address ph and e mail
Nice to have
• Contemporary
smart but organic
Should not have
• no traditional fonts

```html
<!DOCTYPE html>
<html lang="en">
<head>
<meta charset="utf-8">
<title>Carla Mintowe Designs — Business Card</title>
<link rel="stylesheet" href="https://fonts.googleapis.com/css2?family=Titillium+Web:wght@300;400&display=swap">
<style>
  :root {
    --charcoal: #243a33;
    --charcoal-soft: #34493f;
    --lime: #b8f014;
    --white: #ffffff;
    --paper: #ffffff;
  }
  html, body {
    margin: 0;
    padding: 0;
    overflow: hidden;
    background: var(--paper);
  }
  .card {
    position: relative;
    width: 1200px;
    height: 699px;
    background: var(--paper);
    overflow: hidden;
  }
  .card-art {
    position: absolute;
    inset: 0;
  }
  .brand-mark {
    position: absolute;
    left: 179px;
    top: 157px;
    width: 240px;
    height: 240px;
    border-radius: 50%;
    background: var(--charcoal);
  }
  .interior-scene {
    position: absolute;
    left: 740px;
    top: 0;
    width: 400px;
    height: 345px;
    border-radius: 0 0 12px 12px;
    background: linear-gradient(180deg, var(--charcoal-soft), var(--charcoal));
  }
  .wordmark {
    position: absolute;
    left: 74px;
    top: 498px;
    width: 440px;
    font-family: "Titillium Web", sans-serif;
    font-weight: 300;
    color: var(--charcoal);
  }
  .wordmark-name {
    display: block;
    font-size: 66px;
    line-height: 78px;
    letter-spacing: 1px;
    white-space: nowrap;
  }
  .wordmark-tag {
    display: block;
    text-align: right;
    font-size: 40px;
    line-height: 46px;
  }
  .contact {
    position: absolute;
    right: 62px;
    top: 488px;
    margin: 0;
    text-align: right;
    font-family: "Titillium Web", sans-serif;
    font-weight: 400;
    font-size: 27px;
    line-height: 40px;
    color: var(--white);
    font-style: normal;
    white-space: nowrap;
  }
  .contact span { display: block; }
</style>
</head>
<body>
<main class="card">
  <svg class="card-art" width="1200" height="699" viewBox="0 0 1200 699" aria-hidden="true">
    <path class="edge-accent" d="M596 0 Q548 330 590 699 L600 699 L600 0 Z" fill="var(--lime)"/>
    <path class="contact-panel" d="M596 0 L1200 0 L1200 693 L596 693 Q578 340 596 0 Z" fill="var(--charcoal)"/>
  </svg>

  <div class="interior-scene" role="img" aria-label="Line illustration of a framed picture on a wall with two hanging pendant lamps"></div>

  <div class="brand-mark"></div>

  <div class="wordmark">
    <span class="wordmark-name">carlamintowe</span>
    <span class="wordmark-tag">Designs</span>
  </div>

  <address class="contact">
    <span class="contact-business">Carla Mintowe Designs</span>
    <span class="contact-address">58 Fallowmere ave Tindarra 2188 NSW</span>
    <span class="contact-phone">Tel 0417869214</span>
    <span class="contact-email">carlamintowe@quellnet.com.au</span>
  </address>
</main>
</body>
</html>
```